Wellness bold & beautiful PowerPoint Template

I will like a PowerPoint template, matching my brand, designed for my business.
- Some words that describe our brand identity are: wellness, natural, calming, simplicity, clean
- For icons, we prefer line icons.
- Website: http://www.verindale.com/
- PowerPoint board: https://www.pinterest.com/tobramelke/verindale-powerpoint/
- Branding board: https://www.pinterest.com/tobramelke/verindale-branding/
FYI: I am attaching a rough draft of a powerpoint presentation we are preparing
Target Market(s)
Women 23-48 interested in wellness
Industry/Entity Type
Health And Wellness
Font styles to use
Other font styles liked:
- Open Sans, Helvitica, Meddon
Requirements
Must have
- cover page, about page, author page, table of content, table format, graph format, list format, 2 column template.
Nice to have
- time line page sample

```html
<!DOCTYPE html>
<html lang="en">
<head>
<meta charset="UTF-8">
<title>Our Team</title>
<link href="https://fonts.googleapis.com/css2?family=Open+Sans:wght@400;700;800&display=swap" rel="stylesheet">
<style>
  :root {
    --leaf-light: #e3f3cf;
    --leaf-mid: #7cc58a;
    --leaf-deep: #2f9a55;
    --panel: #ffffff;
    --frame-grey: #a6a6a6;
    --text-dark: #1f1f1f;
    --magenta: #b21f8c;
    --green: #649a3f;
    --blue: #2ea8dc;
    --white: #ffffff;
  }
  * { margin: 0; padding: 0; box-sizing: border-box; }
  html, body { width: 1200px; height: 675px; overflow: hidden; }
  body { font-family: "Open Sans", Helvetica, Arial, sans-serif; position: relative; }

  .leaf-backdrop {
    position: absolute; inset: 0;
    background:
      radial-gradient(circle at 20% 30%, var(--leaf-mid) 0%, transparent 45%),
      radial-gradient(circle at 80% 70%, var(--leaf-mid) 0%, transparent 45%),
      linear-gradient(135deg, var(--leaf-light), #bfe3b0 50%, var(--leaf-light));
  }
  .slide-panel {
    position: absolute; left: 78px; top: 45px; width: 1044px; height: 585px;
    background: var(--panel);
  }
  .content-frame {
    position: absolute; left: 100px; top: 66px; width: 998px; height: 542px;
    border: 3px solid var(--frame-grey);
  }
  .title-band {
    position: absolute; left: 100px; top: 66px; width: 998px; height: 70px;
    background: var(--frame-grey);
    display: flex; align-items: center; justify-content: center;
  }
  .title-band h1 {
    color: var(--white); font-weight: 800; font-size: 39px; letter-spacing: 0.5px;
  }
  .member { position: absolute; top: 154px; width: 294px; }
  .member--one { left: 126px; --accent: var(--magenta); }
  .member--two { left: 452px; --accent: var(--green); }
  .member--three { left: 780px; --accent: var(--blue); }

  .portrait {
    display: block; width: 238px; height: 238px; margin-left: 24px;
  }
  .name-tag {
    width: 192px; height: 36px; margin: 18px 0 0 51px;
    background: var(--accent); color: var(--white);
    font-weight: 700; font-size: 18px;
    display: flex; align-items: center; justify-content: center;
  }
  .bio {
    margin-top: 14px; font-size: 14.6px; line-height: 27px;
    color: var(--text-dark); text-align: justify;
  }
</style>
</head>
<body>
  <div class="leaf-backdrop" role="img" aria-label="Pattern of green leaves on a pale green background"></div>
  <div class="slide-panel"></div>
  <div class="content-frame"></div>
  <header class="title-band"><h1>OUR TEAM</h1></header>

  <section class="member member--one">
    <svg class="portrait" viewBox="0 0 238 238" aria-hidden="true">
      <circle cx="119" cy="119" r="119" fill="var(--magenta)"/>
      <rect x="63" y="72" width="103" height="102" rx="5" fill="none" stroke="#fff" stroke-width="10"/>
      <ellipse cx="119" cy="110" rx="16" ry="20" fill="#fff"/>
      <path d="M73 166 C76 146 92 140 108 134 L130 134 C146 140 162 146 165 166 Z" fill="#fff"/>
    </svg>
    <div class="name-tag">NAME #1</div>
    <p class="bio">Lorem ipsum dolor sit amet, consectetur adipiscing elit. Aliquam tincidunt ante nec sem congue convallis. Pellentesque vel mauris quis nisl ornare rutrum in id risus. Proin vehicula ut</p>
  </section>

  <section class="member member--two">
    <svg class="portrait" viewBox="0 0 238 238" aria-hidden="true">
      <circle cx="119" cy="119" r="119" fill="var(--green)"/>
      <rect x="68" y="70" width="103" height="102" rx="5" fill="none" stroke="#fff" stroke-width="10"/>
      <ellipse cx="120" cy="108" rx="16" ry="20" fill="#fff"/>
      <path d="M74 164 C77 144 93 138 109 132 L131 132 C147 138 163 144 166 164 Z" fill="#fff"/>
    </svg>
    <div class="name-tag">NAME #2</div>
    <p class="bio">Lorem ipsum dolor sit amet, consectetur adipiscing elit. Aliquam tincidunt ante nec sem congue convallis. Pellentesque vel mauris quis nisl ornare rutrum in id risus. Proin vehicula ut</p>
  </section>

  <section class="member member--three">
    <svg class="portrait" viewBox="0 0 238 238" aria-hidden="true">
      <circle cx="119" cy="119" r="119" fill="var(--blue)"/>
      <rect x="68" y="72" width="103" height="102" rx="5" fill="none" stroke="#fff" stroke-width="10"/>
      <ellipse cx="120" cy="110" rx="16" ry="20" fill="#fff"/>
      <path d="M74 166 C77 146 93 140 109 134 L131 134 C147 140 163 146 166 166 Z" fill="#fff"/>
    </svg>
    <div class="name-tag">NAME #3</div>
    <p class="bio">Lorem ipsum dolor sit amet, consectetur adipiscing elit. Aliquam tincidunt ante nec sem congue convallis. Pellentesque vel mauris quis nisl ornare rutrum in id risus. Proin vehicula ut</p>
  </section>
</body>
</html>
```